I'm a fishing guide needing a clean, concise design for my business. I'd like to use the cover photo and font design from my website for the background of the business card. My website is:
www.brindlecoveoutfitters.net

Contact Information for Business Card

Capt. Owen Pelk
Fly, Light Tackle, Conventional Gear
Gamefish of Massachusetts
website: www.brindlecoveoutfitters.net
cell: 508-214-9072
email: owen@brindlecoveoutfitters.net

```html
<!DOCTYPE html>
<html lang="en">
<head>
<meta charset="utf-8">
<title>Brindle Cove Outfitters – Business Card</title>
<link href="https://fonts.googleapis.com/css2?family=Open+Sans:wght@700;800&family=Oswald:wght@400;500&display=swap" rel="stylesheet">
<style>
  :root {
    --backdrop: #e4e1dc;
    --slate: #56657f;
    --photo-dark: #3a3140;
    --photo-mid: #6a5a6e;
    --photo-light: #8e8088;
    --photo-accent: #c7694f;
    --ink-light: #ffffff;
  }
  * { margin: 0; padding: 0; box-sizing: border-box; }
  html, body { width: 1200px; height: 800px; overflow: hidden; background: var(--backdrop); }
  .card {
    position: absolute; left: 75px; top: 100px;
    width: 1050px; height: 600px;
    box-shadow: 0 10px 30px rgba(0,0,0,.18);
    overflow: hidden;
  }
  .card-art { position: absolute; inset: 0; }
  .captain {
    position: absolute; top: 16px; right: 36px;
    font: 500 26px "Oswald", sans-serif; color: var(--ink-light);
  }
  .services {
    position: absolute; left: 64px; top: 150px;
    font: 800 38px/1.12 "Open Sans", sans-serif; color: var(--ink-light);
    text-shadow: 0 2px 4px rgba(0,0,0,.35);
  }
  .brand {
    position: absolute; right: 48px; top: 108px;
    display: flex; align-items: center; gap: 14px;
    font: 500 30px/1.1 "Oswald", sans-serif; color: var(--ink-light);
    text-align: right;
  }
  .brand-dot { width: 22px; height: 22px; border-radius: 50%; background: var(--ink-light); flex: none; }
  .contact {
    position: absolute; left: 64px; top: 345px;
    list-style: none;
    font: 400 32px/1.5 "Oswald", sans-serif; color: var(--ink-light);
    text-shadow: 0 2px 4px rgba(0,0,0,.35);
  }
  .contact-label { display: inline-block; width: 48px; font-weight: 500; }
</style>
</head>
<body>
  <div class="card">
    <svg class="card-art" width="1050" height="600" viewBox="0 0 1050 600">
      <defs>
        <linearGradient id="photo-tone" x1="0" y1="1" x2="1" y2="0">
          <stop offset="0" stop-color="var(--photo-light)"/>
          <stop offset="0.45" stop-color="var(--photo-mid)"/>
          <stop offset="0.75" stop-color="var(--photo-dark)"/>
          <stop offset="1" stop-color="var(--photo-accent)"/>
        </linearGradient>
      </defs>
      <rect width="1050" height="600" fill="url(#photo-tone)" role="img" aria-label="Photo of a gamefish with a fly in its mouth"/>
      <polygon class="band-top" points="0,0 1050,0 1050,62 560,62 520,92 0,92" fill="var(--slate)"/>
      <polygon class="band-bottom" points="0,505 500,505 540,445 1050,445 1050,600 0,600" fill="var(--slate)"/>
    </svg>

    <div class="captain">Capt. Owen Pelk</div>

    <div class="brand"><span>Brindle Cove<br>Outfitters</span><span class="brand-dot"></span></div>

    <h1 class="services">Fly, Light Tackle,<br>Conventional Gear Gamefish<br>of Massachusetts</h1>

    <ul class="contact">
      <li><span class="contact-label">P</span>: 508-214-9072</li>
      <li><span class="contact-label">E</span>: owen@brindlecoveoutfitters.net</li>
      <li><span class="contact-label">W</span>: www.brindlecoveoutfitters.net</li>
    </ul>
  </div>
</body>
</html>
```